High impact classy folder for an HVAC and Electrical contractor

We need a folder designed. It needs to be high impact and classy with a rich look to it. We want to cement our branding via the use of the folder so the look will need to have impact with use of our logo and colors.

We want to pull the entire brand look and feel together with this folder. We are going to be making other marketing materials and this is the start of a much larger project. In the ideal situation the winning desginer will continue on with the rest of the projects because they will know how to apply the brand look.

We want to give our local company the feel of a national franchise. Wherein the brand is very prominent and is repeated over and over again.

Use of logo and color scheme will be important.

We like dark backgrounds because they really make the logo pop.

Target Market(s)

homeowners

Font styles to use
Serif

Requirements
Must have
• Logo prominent on the front
• Our Tag Line:
• The Best Way To Live In New Jersey Is With Harbor Vale"
• On the inside pockets:
• Our Phone number: 555-214-6873
• A message to our customers:
• We want to thank you for choosing Harbor Vale Services today
• Our name says it all, because for over 30 years we have prided ourselves on delivering the best service and exceeding our customers' expectations everyday. Whether you need something fixed, replaced or upgraded, no matter how large or small, the dedicated and experts at Harbor Vale Services are here to take care of you. Delivering the right solution for you the first time- everytime - and ensuring you are always 100% satisfied. If for any reason you want to speak with us, please do not hesitate to call or email. Thank you again for choosing Harbor Vale Services.
• On the rear: a graphic that says 24-7 service
• A list of other services we provide:
• Solar
• Generators
• Home Security
• Home Automation
• Home Inspection
• Energy Audits
• 1 Day Bathroom remodles
• Basement Waterproofing
• Garage Doors
• Home Theaters
Nice to have
• I added photos of a flyer and of a mobile website to give an idea of the color scheme as well

```html
<!DOCTYPE html>
<html lang="en">
<head>
<meta charset="utf-8">
<title>Harbor Vale Services – Presentation Folder</title>
<link href="https://fonts.googleapis.com/css2?family=Raleway:ital,wght@0,400;0,600;0,700;1,700&display=swap" rel="stylesheet">
<style>
  :root {
    --stage: #b4b4b4;
    --crimson: #8f1520;
    --crimson-light: #a8222c;
    --cream: #f4ecc4;
    --cream-light: #faf5dc;
    --gold: #f2e3a6;
    --orange: #e88a3a;
    --ink-dark: #5a0d14;
  }
  * { box-sizing: border-box; margin: 0; padding: 0; }
  html, body { width: 842px; height: 1200px; overflow: hidden; }
  body {
    background: var(--stage);
    font-family: "Raleway", Arial, sans-serif;
    position: relative;
  }
  .spread {
    position: absolute;
    left: 51px;
    width: 740px;
    height: 520px;
    display: flex;
    box-shadow: 0 8px 24px rgba(0,0,0,.25);
  }
  .spread--outside { top: 30px; }
  .spread--inside { top: 640px; }
  .panel {
    position: relative;
    width: 370px;
    height: 520px;
    overflow: hidden;
  }
  .panel--back {
    background: linear-gradient(160deg, var(--crimson-light), var(--crimson));
    color: var(--gold);
  }
  .panel--cream {
    background: linear-gradient(160deg, var(--cream-light), var(--cream));
  }
  .frame {
    position: absolute;
    inset: 12px;
    border: 1.5px solid var(--crimson);
    pointer-events: none;
  }
  .panel--back .frame { border-color: var(--gold); opacity: .8; }

  /* back panel */
  .back-content {
    position: absolute;
    inset: 60px 30px 40px;
    text-align: center;
  }
  .brand-name {
    font-family: "Raleway", Arial, sans-serif;
    font-weight: 700;
    line-height: 1.05;
  }
  .back-content .brand-name { font-size: 40px; color: var(--gold); margin-bottom: 34px; }
  .provide-title { font-size: 10px; font-weight: 700; letter-spacing: .5px; margin-bottom: 6px; }
  .service-list { font-size: 10.5px; line-height: 1.45; margin-bottom: 18px; }
  .service-badge { font-size: 13px; font-weight: 700; font-style: italic; margin-bottom: 18px; }
  .licenses { font-size: 9.5px; line-height: 1.5; margin-bottom: 14px; }
  .address { font-size: 9.5px; margin-bottom: 6px; }
  .web-pill {
    display: inline-block;
    background: var(--orange);
    color: var(--ink-dark);
    font-size: 10px;
    font-weight: 600;
    padding: 3px 16px;
    border-radius: 10px;
  }

  /* front panel */
  .front-mark {
    position: absolute;
    top: 170px;
    left: 0; right: 0;
    display: flex;
    flex-direction: column;
    align-items: center;
    gap: 12px;
  }
  .front-mark .brand-name { font-size: 36px; color: var(--crimson); text-align: center; }
  .mark-square { width: 14px; height: 14px; background: var(--crimson); }
  .tagline {
    position: absolute;
    bottom: 36px;
    left: 0; right: 0;
    display: flex;
    align-items: center;
    justify-content: center;
    gap: 6px;
    font-size: 9.5px;
    color: var(--crimson);
  }
  .tagline-rule { width: 22px; height: 1px; background: var(--crimson); }

  /* inside */
  .watermark {
    position: absolute;
    top: 110px;
    left: 0; right: 0;
    text-align: center;
    font-size: 48px;
    color: var(--crimson);
    opacity: .06;
  }
  .pocket {
    position: absolute;
    left: 0; right: 0; bottom: 0;
    height: 200px;
    background: linear-gradient(160deg, var(--crimson-light), var(--crimson));
    color: var(--cream-light);
    padding: 28px 30px;
    box-shadow: 0 -4px 10px rgba(0,0,0,.15);
  }
  .pocket-message { font-size: 10px; line-height: 1.55; }
  .pocket--thanks {
    display: flex;
    flex-direction: column;
    align-items: center;
    justify-content: center;
    text-align: center;
  }
  .thanks-line { font-size: 12.5px; font-weight: 600; line-height: 1.4; }
  .phone-row { display: flex; align-items: center; gap: 8px; margin-top: 6px; }
  .phone-rule { width: 30px; height: 1px; background: var(--cream-light); }
  .phone-number { font-size: 21px; font-weight: 700; letter-spacing: 1px; }
</style>
</head>
<body>
  <section class="spread spread--outside" aria-label="Folder outside">
    <div class="panel panel--back">
      <div class="frame"></div>
      <div class="back-content">
        <p class="brand-name">Harbor Vale<br>Services</p>
        <p class="provide-title">WE PROVIDE</p>
        <p class="service-list">
          Solar • Generators • Home Security<br>
          Home Automation • Home Inspection • Energy Audits<br>
          1 Day Bathroom remodles • Basement Waterproofing<br>
          Garage Doors • Home Theaters
        </p>
        <p class="service-badge">A graphic that says 24-7 service</p>
        <p class="licenses">
          NJ HVAC License # 482 | NJ Electrical License # 20514<br>
          NJ Home Improvement Business Registration # 13VH00218844
        </p>
        <p class="address">P.O.Box 412, Lakeside, NJ 07000</p>
        <span class="web-pill">www.HarborValeServices.com</span>
      </div>
    </div>
    <div class="panel panel--cream">
      <div class="frame"></div>
      <div class="front-mark">
        <span class="mark-square"></span>
        <p class="brand-name">Harbor Vale<br>Services</p>
      </div>
      <p class="tagline"><span class="tagline-rule"></span>The Best Way To Live In New Jersey Is With Harbor Vale<span class="tagline-rule"></span></p>
    </div>
  </section>

  <section class="spread spread--inside" aria-label="Folder inside">
    <div class="panel panel--cream">
      <p class="watermark brand-name">Harbor Vale<br>Services</p>
      <div class="pocket">
        <p class="pocket-message">Our name says it all, because for over 30 years we have prided ourselves on delivering the best service and exceeding our customers' expectations everyday. Whether you need something fixed, replaced or upgraded, no matter how large or small, the dedicated experts at Harbor Vale Services are here to take care of you. Delivering the right solution for you the first time – everytime – and ensuring you are always 100% satisfied. If for any reason you want to speak with us, please do not hesitate to call or email. Thank you again for choosing Harbor Vale Services.</p>
      </div>
    </div>
    <div class="panel panel--cream">
      <p class="watermark brand-name">Harbor Vale<br>Services</p>
      <div class="pocket pocket--thanks">
        <p class="thanks-line">We want to thank you for<br>choosing Harbor Vale Services today</p>
        <div class="phone-row"><span class="phone-rule"></span><span class="phone-number">555-214-6873</span><span class="phone-rule"></span></div>
      </div>
    </div>
  </section>
</body>
</html>
```